Business Card Design

Hoping for a black background business card, minimalistic design.
With the Marble Crest logo you created in white.

I would like to include:
My Name and title
Address (street address)
Reception: (phone number)
Fax: (fax number)
Reception: (email address)
Direct email: (email address)
Instagram: (ig handle)

```html
<!DOCTYPE html>
<html lang="en">
<head>
<meta charset="UTF-8">
<title>Marble Crest — Business Card</title>
<link href="https://fonts.googleapis.com/css2?family=Poppins:wght@300;400;600&family=Montserrat:wght@400;500&display=swap" rel="stylesheet">
<style>
  :root {
    --backdrop: #3b3e44;
    --card: #0d0d0e;
    --ink: #ffffff;
    --ink-soft: #d9d9d9;
    --rule: #5a5a5a;
    --ghost: #1f1f21;
  }
  * { margin: 0; padding: 0; box-sizing: border-box; }
  html, body { width: 1200px; height: 900px; overflow: hidden; }
  body {
    background: var(--backdrop);
    font-family: "Poppins", sans-serif;
    color: var(--ink);
    position: relative;
  }
  .card {
    position: absolute;
    width: 520px;
    height: 300px;
    background: var(--card);
    border-radius: 4px;
    overflow: hidden;
    box-shadow: 0 18px 40px rgba(0,0,0,0.45);
  }
  .card--back { left: 50px; top: 400px; }
  .card--front { left: 630px; top: 200px; }

  /* back: contact side */
  .contact { position: absolute; left: 30px; top: 30px; width: 260px; }
  .contact__name { font-weight: 600; font-size: 15px; letter-spacing: 0.02em; text-transform: uppercase; }
  .contact__title { font-weight: 300; font-size: 12px; color: var(--ink-soft); margin-bottom: 10px; }
  .contact__rule { height: 1px; background: var(--rule); width: 210px; margin-bottom: 10px; }
  .contact__list { list-style: none; }
  .contact__item { display: flex; align-items: center; gap: 8px; font-size: 11px; font-weight: 300; line-height: 18px; }
  .contact__item svg { width: 10px; height: 10px; flex: none; fill: var(--ink); }
  .contact__address { margin-top: 12px; font-size: 11px; font-weight: 300; line-height: 16px; }

  .brand-mark {
    position: absolute; right: 34px; bottom: 28px;
    display: flex; flex-direction: column; align-items: center; gap: 10px;
  }
  .brand-mark__circle {
    width: 140px; height: 140px; border-radius: 50%;
    border: 7px solid var(--ink);
  }
  .brand-name {
    font-family: "Montserrat", sans-serif; font-weight: 500;
    letter-spacing: 0.14em; text-transform: uppercase; color: var(--ink);
  }
  .brand-mark .brand-name { font-size: 13px; }

  /* front: wordmark side */
  .ghost-circle {
    position: absolute; right: -40px; top: 70px;
    width: 270px; height: 270px; border-radius: 50%;
    border: 12px solid var(--ghost);
  }
  .lockup {
    position: absolute; left: 44px; top: 96px;
    display: flex; align-items: center; gap: 14px;
  }
  .lockup__circle { width: 46px; height: 46px; border-radius: 50%; border: 3px solid var(--ink); }
  .lockup__divider { width: 1px; height: 64px; background: var(--ink-soft); }
  .lockup .brand-name { font-size: 30px; }
  .front__web {
    position: absolute; left: 168px; top: 190px;
    font-size: 11px; letter-spacing: 0.18em; text-transform: uppercase; color: var(--ink-soft);
  }
</style>
</head>
<body>

  <section class="card card--front">
    <div class="ghost-circle"></div>
    <div class="lockup">
      <div class="lockup__circle"></div>
      <div class="lockup__divider"></div>
      <span class="brand-name">Marble Crest</span>
    </div>
    <p class="front__web">www.marblecrest-site.com</p>
  </section>

  <section class="card card--back">
    <div class="contact">
      <h1 class="contact__name">Daniel Whitmore</h1>
      <p class="contact__title">CEO/Founder</p>
      <div class="contact__rule"></div>
      <ul class="contact__list">
        <li class="contact__item">
          <svg viewBox="0 0 10 10"><path d="M2 0.5 L3.6 2.6 L2.8 3.6 Q4 6 6.4 7.2 L7.4 6.4 L9.5 8 L8.4 9.5 Q1 8 0.5 1.6 Z"/></svg>
          555 218 4730
        </li>
        <li class="contact__item">
          <svg viewBox="0 0 10 10"><rect x="2.5" y="0.5" width="5" height="3"/><rect x="0.5" y="3.5" width="9" height="4" rx="0.6"/><rect x="2.5" y="6.5" width="5" height="3"/></svg>
          555 218 4731
        </li>
        <li class="contact__item">
          <svg viewBox="0 0 10 10"><rect x="0.5" y="2" width="9" height="6.5"/><path d="M0.5 2 L5 5.6 L9.5 2" stroke="#0d0d0e" stroke-width="0.9" fill="none"/></svg>
          daniel@marblecrest-mail.com
        </li>
        <li class="contact__item">
          <svg viewBox="0 0 10 10"><rect x="0.5" y="2" width="9" height="6.5"/><path d="M0.5 2 L5 5.6 L9.5 2" stroke="#0d0d0e" stroke-width="0.9" fill="none"/></svg>
          direct@marblecrest-mail.com
        </li>
        <li class="contact__item">
          <svg viewBox="0 0 10 10"><circle cx="5" cy="5" r="4.3" fill="none" stroke="#fff" stroke-width="1"/><ellipse cx="5" cy="5" rx="1.8" ry="4.3" fill="none" stroke="#fff" stroke-width="0.8"/><line x1="0.7" y1="5" x2="9.3" y2="5" stroke="#fff" stroke-width="0.8"/></svg>
          www.marblecrest-site.com
        </li>
        <li class="contact__item">
          <svg viewBox="0 0 10 10"><circle cx="5" cy="5" r="4.3" fill="none" stroke="#fff" stroke-width="1"/></svg>
          @marblecrest.co
        </li>
      </ul>
      <p class="contact__address">418 Harbor Lane West<br>Suite 210, Millbrook<br>OR 97012</p>
    </div>
    <div class="brand-mark">
      <div class="brand-mark__circle"></div>
      <span class="brand-name">Marble Crest</span>
    </div>
  </section>

</body>
</html>
```